MLOrchard
Home Page
MLOrchard -
Creative Brief
maplethornorchard.example
This company is comprised of two things: 1) a produce market that sells a variety of berries and 2) a strawberry farm where you can pick your own and participate in a variety of activities for the family.
Likes www.brookvalegroves.example. Likes the pictures of families and children having fun. Site should present a fun environment.
Friendly
For Children
Fun
Red for strawberries
Green for strawberries
Yellow to go with logo
below header
www.brookvalegroves.example
There needs to be a horizontal slideshow on the home page. The slideshow should span the width of the site. There should be a top horizontal banner with the main navigation bar running horizontally under the banner and then the slideshow should be under the main horizontal navigation. Site should be approximately 1,050 pixels wide and about 750-850 pixels long. The main navigation bar should contain the following links: Home, Our History, Berry Farm, Berry Market, Map/Directions/Contact, Coupons/Specials, Sign up for Specials

```html
<!DOCTYPE html>
<html lang="en">
<head>
<meta charset="utf-8">
<title>MLOrchard – Home</title>
<link rel="stylesheet" href="https://fonts.googleapis.com/css2?family=Lobster&family=Patrick+Hand&family=Open+Sans:wght@400;700;800&family=Tinos:wght@400;700&display=swap">
<style>
:root{
  --berry-red:#c8141c;
  --berry-dark:#8e0b10;
  --berry-light:#e8434a;
  --leaf-green:#3f9e3c;
  --leaf-light:#6cc063;
  --leaf-dark:#2b7a2a;
  --sun-yellow:#f4d55a;
  --sun-light:#fbe98f;
  --ink:#222;
  --muted:#444;
  --white:#fff;
}
*{box-sizing:border-box;margin:0;padding:0}
html,body{width:1200px;height:809px;overflow:hidden;background:var(--white)}
body{position:relative;font-family:"Open Sans",Arial,sans-serif;color:var(--ink)}
.abs{position:absolute}

/* header */
.brand{left:144px;top:34px;display:flex;align-items:center;gap:12px}
.brand-dot{width:46px;height:46px;border-radius:50%;background:var(--berry-red)}
.brand-name{font-weight:800;font-size:26px;color:var(--berry-red)}
.phone{left:583px;top:90px;font-family:"Patrick Hand",cursive;font-size:30px;line-height:34px;color:var(--ink);letter-spacing:1px;white-space:nowrap}
.banner{left:100px;top:132px;width:1000px;height:127px;
  background:linear-gradient(180deg,var(--berry-light) 0%,var(--berry-red) 45%,var(--berry-dark) 100%)}
.banner-title{left:50px;top:14px;font-family:"Lobster",cursive;font-size:36px;line-height:44px;color:var(--white);white-space:nowrap;text-shadow:0 2px 3px rgba(0,0,0,.35)}
.banner-sub{left:92px;top:62px;font-family:"Lobster",cursive;font-size:34px;line-height:44px;color:var(--white);white-space:nowrap;text-shadow:0 2px 3px rgba(0,0,0,.35)}
.banner-tag{left:418px;top:76px;font-family:"Lobster",cursive;font-size:26px;line-height:34px;color:var(--white);white-space:nowrap;transform:rotate(-11deg);transform-origin:left bottom}
.hero-berry{left:850px;top:4px;width:236px;height:256px;
  border-radius:50% 50% 46% 46% / 42% 42% 58% 58%;
  background:radial-gradient(circle at 40% 38%,#f04a3e 0%,#d31515 55%,#9c0c0c 100%)}

/* navigation */
.main-nav{left:100px;top:278px;width:1000px;height:48px;border-radius:10px;
  background:linear-gradient(180deg,var(--leaf-light),var(--leaf-green) 55%,var(--leaf-dark))}
.main-nav a{position:absolute;top:13px;font-weight:800;font-size:16px;line-height:22px;color:var(--white);text-decoration:none;letter-spacing:.2px;white-space:nowrap}
.main-nav a.current{color:var(--berry-red);text-decoration:underline}

/* slideshow */
.slide{top:331px;width:192px;height:202px}
.slide-1{left:187px;background:linear-gradient(135deg,#5c9a3a,#d0241c 55%,#7bb04a)}
.slide-2{left:396px;background:linear-gradient(160deg,#e0302a,#b3100f 60%,#e85040)}
.slide-3{left:607px;background:linear-gradient(140deg,#3e7a2e,#c9a28a 50%,#4d8b35)}
.slide-4{left:818px;background:linear-gradient(180deg,#a7c66b,#4f8a34 60%,#3d6f2a)}
.slide-arrow{top:412px;width:24px;height:40px}

/* content */
.section-title{font-family:"Tinos",serif;font-size:22px;line-height:26px;color:var(--ink);top:560px;white-space:nowrap}
.thumb{top:595px;width:115px;height:101px}
.thumb-farm{left:149px;background:linear-gradient(150deg,#5d9a3d,#c9221a 60%,#6aa144)}
.thumb-market{left:473px;background:linear-gradient(150deg,#f0e6e0,#d62a22 55%,#f5f0ea)}
.teaser{top:590px;width:180px;font-size:12.5px;line-height:16px;color:var(--muted);font-family:Arial,sans-serif}
.teaser h3{font-size:12.5px;font-weight:700;color:var(--ink);margin-bottom:4px}
.read-more{top:683px;font-size:11.5px;color:var(--ink);text-decoration:underline;font-family:Arial,sans-serif}

/* specials */
.specials{left:828px;top:559px;width:228px;height:173px;border-radius:4px;
  background:radial-gradient(circle at 30% 30%,var(--sun-light),var(--sun-yellow))}
.specials-icon{left:10px;top:8px;width:55px;height:62px;border-radius:6px;
  background:radial-gradient(circle at 45% 55%,#e33a2e,#b10f10 70%,#4d8a2e)}
.specials-title{left:72px;top:10px;font-family:"Tinos",serif;font-size:22px;line-height:24px;color:var(--ink)}
.field-label{left:24px;font-size:12px;font-family:Arial,sans-serif;color:var(--ink)}
.field{left:65px;width:146px;height:17px;background:var(--white);border:1px solid #c9a93e}
.submit{left:77px;top:142px;width:67px;height:22px;border-radius:3px;background:#3a3a3a;color:var(--white);
  font-size:12px;font-family:Arial,sans-serif;text-align:center;line-height:22px}

/* footer */
.site-footer{left:100px;top:737px;width:1000px;height:72px;background:linear-gradient(180deg,var(--berry-red),var(--berry-dark))}
.site-footer p{position:absolute;left:18px;font-size:12px;color:var(--white);font-family:Arial,sans-serif;white-space:nowrap}
.social{top:732px;width:50px;height:50px;border-radius:8px}
.social-1{left:945px;background:#4ab3e6}
.social-2{left:1010px;background:#3b7fd0}
</style>
</head>
<body>

<header>
  <div class="abs brand"><span class="brand-dot"></span><span class="brand-name">Maplethorn Orchard</span></div>
  <div class="abs phone">Call :555 014 2090</div>
  <div class="abs banner">
    <div class="abs banner-title">Welcome to Maplethorn Orchard</div>
    <div class="abs banner-sub">Farm &amp; Market !</div>
    <div class="abs banner-tag">Pick Up your Strawberries</div>
  </div>
  <div class="abs hero-berry" role="img" aria-label="Large ripe strawberry with green leaves"></div>
</header>

<nav class="abs main-nav">
  <a class="current" style="left:44px" href="#">HOME</a>
  <a style="left:130px" href="#">OUR HISTORY</a>
  <a style="left:267px" href="#">BERRY FARM</a>
  <a style="left:392px" href="#">BERRY MARKET</a>
  <a style="left:538px" href="#">DIRECTIONS</a>
  <a style="left:663px" href="#">COUPONS</a>
  <a style="left:771px" href="#">SPECIALS</a>
  <a style="left:872px" href="#">CONTACT US</a>
</nav>

<section class="slideshow">
  <svg class="abs slide-arrow" style="left:144px" viewBox="0 0 24 40"><path d="M20 4 L6 20 L20 36" fill="none" stroke="#3f9e3c" stroke-width="5"/></svg>
  <div class="abs slide slide-1" role="img" aria-label="Strawberries growing on the plant"></div>
  <div class="abs slide slide-2" role="img" aria-label="Close-up of fresh picked strawberries"></div>
  <div class="abs slide slide-3" role="img" aria-label="Child picking strawberries in the field"></div>
  <div class="abs slide slide-4" role="img" aria-label="Children walking along the strawberry rows"></div>
  <svg class="abs slide-arrow" style="left:1032px" viewBox="0 0 24 40"><path d="M4 4 L18 20 L4 36" fill="none" stroke="#3f9e3c" stroke-width="5"/></svg>
</section>

<main>
  <h2 class="abs section-title" style="left:144px">Welcome&nbsp; to MLOrchard</h2>
  <div class="abs thumb thumb-farm" role="img" aria-label="Strawberries ripening in the field"></div>
  <div class="abs teaser" style="left:278px">
    <h3>Lorem ipsum dolor sit</h3>
    <p>Lorem ipsum dolor sit amet, consectetuer adipiscing elit, sed to diam nonummy nibh euismod tincidunt ut</p>
  </div>
  <a class="abs read-more" style="left:350px" href="#">Read More</a>

  <h2 class="abs section-title" style="left:473px">Farm Market</h2>
  <div class="abs thumb thumb-market" role="img" aria-label="Strawberry desserts from the market"></div>
  <div class="abs teaser" style="left:600px">
    <h3>Lorem ipsum dolor sit</h3>
    <p>Lorem ipsum dolor sit amet, consectetuer adipiscing elit, sed to diam nonummy nibh euismod tincidunt ut</p>
  </div>
  <a class="abs read-more" style="left:694px" href="#">Read More</a>

  <aside class="abs specials">
    <div class="abs specials-icon" role="img" aria-label="Strawberry"></div>
    <div class="abs specials-title">Sign up for<br>Specials</div>
    <span class="abs field-label" style="top:82px">Email :</span>
    <span class="abs field" style="top:81px"></span>
    <span class="abs field-label" style="top:108px">Name</span>
    <span class="abs field" style="top:106px"></span>
    <span class="abs submit">Submit</span>
  </aside>
</main>

<footer class="abs site-footer">
  <p style="top:10px">Maplethorn Orchard: 410 Quarry Lane Fernwick, VA 20199 Harvest Hotline: 555-014-7731</p>
  <p style="top:30px">contact_us@maplethornorchard.example</p>
  <p style="top:52px">Copyright © 2011 Maplethorn Orchard</p>
</footer>
<span class="abs social social-1"></span>
<span class="abs social social-2"></span>

</body>
</html>
```